Flyer Design

this must be private.
It is for an GT convention.
If I can have direct email to you I will send in last years Flyer with up dated details.

Thank you

Mrs R T Hollis

```html
<!DOCTYPE html>
<html lang="en">
<head>
<meta charset="utf-8">
<title>GT Convention Flyer</title>
<link href="https://fonts.googleapis.com/css2?family=Jost:wght@400;500;600;700;800&display=swap" rel="stylesheet">
<style>
:root{
  --sky:#5fb4ec;
  --ocean:#1d6fd6;
  --deep:#0f3fa8;
  --panel-edge:#3a8fe0;
  --ink:#0d0d1a;
  --rule:#2f86e0;
  --white:#ffffff;
}
*{margin:0;padding:0;box-sizing:border-box}
html,body{width:1200px;height:850px;overflow:hidden}
body{font-family:"Jost",sans-serif;color:var(--ink);background:var(--deep)}
.flyer{position:relative;width:1200px;height:850px;overflow:hidden;
  background:radial-gradient(ellipse at 85% 45%,#7cc6f4 0%,var(--sky) 18%,var(--ocean) 50%,var(--deep) 100%)}
.swirl-backdrop{position:absolute;inset:0}
.info-panel{position:absolute;left:48px;top:42px;width:510px;height:760px;border-radius:22px;
  background:rgba(236,245,253,.93);border:2px solid var(--panel-edge)}
.photo{position:absolute;border-radius:50%;border:3px solid var(--white)}
.photo-buffet{left:262px;top:2px;width:148px;height:142px;background:radial-gradient(circle at 40% 50%,#d9a56a,#8c4a2a 70%,#4a2a1c)}
.photo-hotel{left:388px;top:2px;width:192px;height:192px;background:linear-gradient(180deg,#a9cde9 0%,#d8d2c4 40%,#8d8a6f 60%,#4f7a3a 100%)}
.photo-room{left:420px;top:145px;width:166px;height:166px;background:radial-gradient(circle at 55% 60%,#c9bfa8,#7d7a66 60%,#3f3a2f)}
.hotel-name{position:absolute;left:70px;top:78px;font-size:34px;font-weight:700;line-height:31px}
.panel-text{position:absolute;left:70px;font-size:13.5px;font-weight:400}
.hotel-desc{top:151px;width:470px;line-height:19.2px}
.photo-clearance{float:right;width:128px;height:154px}
.section-title{position:absolute;left:48px;width:510px;text-align:center;font-size:33px;font-weight:800}
.reg-title{top:362px}
.book-title{top:531px}
.reg-text{top:410px;width:468px;line-height:19px}
.reg-text p+p{margin-top:4px}
.rooms-title{position:absolute;left:70px;top:578px;font-size:22px;font-weight:600}
.rooms-text{top:608px;width:470px;line-height:18px}
.rooms-text p+p{margin-top:3px}
.programme-title{position:absolute;left:668px;top:58px;font-size:32px;font-weight:800;color:var(--white)}
.programme-note{position:absolute;left:650px;top:110px;font-size:14px;font-weight:600;color:var(--white)}
.day-box{position:absolute;left:650px;width:508px;border-radius:20px;
  background:rgba(230,242,252,.9);border:2px solid #9fd0f6;padding:16px 16px 0 16px}
.day-fri{top:157px;height:214px}
.day-sat{top:383px;height:222px;padding-top:14px}
.day-sun{top:618px;height:190px;padding-top:14px}
.day-title{font-size:15px;font-weight:700;line-height:20px;padding-bottom:5px;border-bottom:1.5px solid var(--rule)}
.slot{display:flex;font-size:15px;line-height:21px;font-weight:500;border-bottom:1.5px solid var(--rule);padding-top:1px}
.day-title+.slot{margin-top:9px}
.slot-time{width:217px;flex:none}
.slot-event small{font-size:10px}
.slot-last{border-bottom:none}
.slot-note{font-style:italic;display:block;line-height:19px}
</style>
</head>
<body>
<div class="flyer">
  <svg class="swirl-backdrop" width="1200" height="850" role="img" aria-label="Swirling blue concentric ring background pattern">
    <defs>
      <radialGradient id="glow" cx="0.8" cy="0.45" r="0.6">
        <stop offset="0" stop-color="#bfe6ff" stop-opacity=".45"/>
        <stop offset="1" stop-color="#bfe6ff" stop-opacity="0"/>
      </radialGradient>
    </defs>
    <rect width="1200" height="850" fill="url(#glow)"/>
  </svg>

  <section class="info-panel"></section>
  <div class="photo photo-buffet" role="img" aria-label="Photo of hotel carvery buffet"></div>
  <div class="photo photo-hotel" role="img" aria-label="Photo of the hotel building with gardens"></div>
  <div class="photo photo-room" role="img" aria-label="Photo of a twin hotel bedroom"></div>

  <h1 class="hotel-name">Headland<br>Hotel</h1>
  <p class="panel-text hotel-desc"><span class="photo-clearance"></span>Very popular with GT convention attendees, this MTA three star hotel is set in a prominent sea front position. The hotel is located on a tranquil grassy peninsula surrounded by 5 acres of gardens, which leads to a sandy bay in the quiet parish of the Dunes. All bedrooms en-suite with satellite TV, coffee and tea making facilites. There is a volleyball court, putting green, croquet lawn, petanque area and children’s playground. There are also gentle walks around Grand Sable Bay. For details regarding alternative accommodation venues, air/sea travel etc., log onto Island Tourist Board Official Website: www.visitislandbay.com</p>

  <h2 class="section-title reg-title">Registration:</h2>
  <div class="panel-text reg-text">
    <p>A registration fee of £8.95 will apply, which includes unlimited tea/coffee, cordial/water throughout the day over the three days. This fee goes directly to the hotel to cover the cost of the weekend’s events.</p>
    <p>All attendees MUST register and badges should be worn to all meetings and functions over the weekend. We recommend you register as soon as you check in at the hotel.</p>
  </div>

  <h2 class="section-title book-title">How to book:</h2>
  <h3 class="rooms-title">Bedrooms</h3>
  <div class="panel-text rooms-text">
    <p>£70 per room per night bed and breakfast in double/twin occupancy<br>£103 per room per night half board in double/twin occupancy</p>
    <p>£51 per room per night bed and breakfast in sole occupancy<br>£67.50 per room per night half board in sole occupancy</p>
    <p>Deposit per room required at time of booking will be £60.</p>
    <p>Friday Dinner £17.50&nbsp; Saturday £19.50</p>
    <p>To book please use the following contact details quoting<br>“Friends of Tom R Convention”</p>
    <p>Tel: 04100 555012 or email bookings@headland-hotel.example</p>
  </div>

  <h2 class="programme-title">CONVENTION PROGRAMME</h2>
  <p class="programme-note">An early bird meeting may be available at the Hotel Thursday evening.</p>

  <section class="day-box day-fri">
    <h3 class="day-title">Friday 6th November</h3>
    <div class="slot"><span class="slot-time">3.30pm - onwards</span><span class="slot-event">Registration GT and Kin-Link</span></div>
    <div class="slot"><span class="slot-time">6.30pm - 8.00pm</span><span class="slot-event">Carvery Buffet</span></div>
    <div class="slot"><span class="slot-time">8.30pm - 8.50pm</span><span class="slot-event">GT and Kin-Link Welcome Meeting</span></div>
    <div class="slot"><span class="slot-time">9.00pm - 10.30pm</span><span class="slot-event">GT Closed Meeting</span></div>
    <div class="slot"><span class="slot-time">9.00pm - 10.30pm</span><span class="slot-event">Kin-Link Closed Meeting</span></div>
    <div class="slot"><span class="slot-time">Midnight till Late</span><span class="slot-event">GT ‘Night Owls’ Meeting</span></div>
  </section>

  <section class="day-box day-sat">
    <h3 class="day-title">Saturday 7th November</h3>
    <div class="slot"><span class="slot-time">10.00am - 11.30am</span><span class="slot-event">GT Closed Meeting</span></div>
    <div class="slot"><span class="slot-time">10.00am - 11.30am</span><span class="slot-event">Kin-Link Closed Meeting</span></div>
    <div class="slot"><span class="slot-time">12.00pm - onwards</span><span class="slot-event">Lunch <small>(please make your own arrangements)</small></span></div>
    <div class="slot"><span class="slot-time">3.00pm - 4.30pm</span><span class="slot-event">GT Open Meeting</span></div>
    <div class="slot"><span class="slot-time">3.00pm - 4.30pm</span><span class="slot-event">Kin-Link Open Meeting</span></div>
    <div class="slot"><span class="slot-time">7.00pm - 12.00am</span><span class="slot-event">Gala Dinner and Disco</span></div>
    <div class="slot"><span class="slot-time">Midnight till Late</span><span class="slot-event">GT ‘Night Owls’ Meeting</span></div>
  </section>

  <section class="day-box day-sun">
    <h3 class="day-title">Sunday 8th November</h3>
    <div class="slot"><span class="slot-time">9.30am - 10.15am</span><span class="slot-event">Open Spiritual Meeting</span></div>
    <div class="slot"><span class="slot-time">10.45am - 12.45pm</span><span class="slot-event">GT and Kin-Link Shared Platform</span></div>
    <div class="slot slot-last"><span class="slot-time">1.15pm - 3.00pm</span><span class="slot-event">Lunch and Farwells<span class="slot-note">(Remember if you require Sunday<br>Lunch, please book in advance<br>directly with the Hotel reception)</span></span></div>
  </section>
</div>
</body>
</html>
```